Catalogue Design Project

Hi Guys

We are a wine mail order company,
Enclosed is a detailed description of what we are after as well as examples from our competitors.

Feel free to be creative

Cheers

Dermot Whitby

Target market

- Middle aged wine drinkers of a rural background
- Gender, Male
- Occupation, Farmers

It Company

```html
<!DOCTYPE html>
<html lang="en">
<head>
<meta charset="utf-8">
<title>Coorong Cellars – Catalogue Covers</title>
<link rel="stylesheet" href="https://fonts.googleapis.com/css2?family=Marcellus&family=Philosopher&display=swap">
<style>
  :root {
    --canvas: #ffffff;
    --panel-grey: #a1a1a1;
    --wine-red: #e42229;
    --band-black: #1d1a1b;
    --shadow: #3f3b3b;
    --flap: #6e6c6c;
    --white: #ffffff;
    --cream: #f7ecd0;
  }
  * { margin: 0; padding: 0; box-sizing: border-box; }
  html, body { width: 1200px; height: 777px; overflow: hidden; background: var(--canvas); }
  .canvas { position: relative; width: 1200px; height: 777px; }

  .cover {
    position: absolute; top: 17px; width: 574px; height: 743px;
    background: var(--panel-grey); overflow: hidden;
  }
  .cover--front { left: 17px; }
  .cover--back { left: 607px; }

  .pennant { position: absolute; left: 0; top: 0; width: 574px; height: 743px; }

  .brand {
    position: absolute; left: 0; width: 100%;
    display: flex; flex-direction: column; align-items: center;
  }
  .brand__mark { width: 44px; height: 44px; border-radius: 50%; margin-bottom: 14px; }
  .brand__name {
    font-family: "Marcellus", serif; font-size: 31px; letter-spacing: 0.5px;
    line-height: 1; white-space: nowrap;
  }

  .cover--front .brand { top: 102px; left: 105px; width: 364px; }
  .cover--front .brand__mark { background: var(--white); }
  .cover--front .brand__name { color: var(--white); }

  .contact {
    position: absolute; left: 105px; width: 364px; text-align: center;
    font-family: "Philosopher", sans-serif; font-size: 12.5px; color: var(--cream);
  }
  .contact--address { top: 248px; }
  .contact--email { top: 278px; }

  .back-block {
    position: absolute; left: 75px; top: 98px; width: 422px; height: 546px;
    background: var(--wine-red);
  }
  .band-flaps { position: absolute; left: 0; top: 0; width: 574px; height: 743px; }
  .band {
    position: absolute; left: 32px; top: 267px; width: 509px; height: 208px;
    background: var(--band-black);
  }
  .cover--back .brand { top: 48px; left: 0; width: 509px; }
  .cover--back .brand__mark { background: var(--wine-red); }
  .cover--back .brand__name { color: var(--white); }
</style>
</head>
<body>
<main class="canvas">

  <section class="cover cover--front">
    <svg class="pennant" viewBox="0 0 574 743" aria-hidden="true">
      <polygon fill="var(--shadow)" points="110,0 474,0 474,340 258,378 110,344"/>
      <polygon fill="var(--wine-red)" points="105,0 469,0 469,335 287,374 105,335"/>
    </svg>
    <div class="brand">
      <span class="brand__mark"></span>
      <span class="brand__name">Coorong Cellars</span>
    </div>
    <p class="contact contact--address">14 Wattle Street, Adelaide 5000</p>
    <p class="contact contact--email">orders@coorongcellars.com</p>
  </section>

  <section class="cover cover--back">
    <div class="back-block"></div>
    <svg class="band-flaps" viewBox="0 0 574 743" aria-hidden="true">
      <polygon fill="var(--flap)" points="32,267 75,259 75,267"/>
      <polygon fill="var(--flap)" points="497,475 541,475 497,483"/>
    </svg>
    <div class="band">
      <div class="brand">
        <span class="brand__mark"></span>
        <span class="brand__name">Coorong Cellars</span>
      </div>
    </div>
  </section>

</main>
</body>
</html>
```